Zenvok - Property Management Company Listings - PSD / uncoded only

Our site simply connects property owners with property managers. I’m asking you to create 2 pages, 1 homepage and 1 page that lists of property management companies. Build with Responsive Design in mind. PSD/uncoded files only. Help us create a great site!
Example competitor sites:
http://www.everyleaseguildhall.example/
http://www.tendourestates.example/
Inspired by these sites:
http://www.quorvix.example/
http://www.bespokuna.example/
http://www.fundlo.example/
https://www.tripnook.example/
I've attached the logo as well as 2 picture files that you can consider using.
• Zenvok Logo Colors: Yellow: HTML code: #FBC30A, RGB code: R: 251 G: 195 B: 10 Grey: HTML code: #4E4C4D, RGB code: R: 78 G: 76 B: 77
• The picture files are optional.
o One picture is of houses and neighborhood.
o The other is of a professional woman on the phone. Please do not use the professional woman as a large primary image. You can use the professional woman photo as a smaller photo and not the main photo.
• Please bring your own pictures and graphics too. Don't feel like you need to use mine.
Thank you!
Property Management

```html
<!DOCTYPE html>
<html lang="en">
<head>
<meta charset="utf-8">
<title>Zenvok – Property Management</title>
<link href="https://fonts.googleapis.com/css2?family=Raleway:wght@400;600;700;800&family=Open+Sans:wght@400;600;700&display=swap" rel="stylesheet">
<style>
:root{
  --yellow:#fbc30a;
  --grey:#4e4c4d;
  --dark:#3a393a;
  --darker:#2e2d2e;
  --ink:#333;
  --muted:#8a8a8a;
  --line:#e2e2e2;
  --white:#fff;
}
*{box-sizing:border-box;margin:0;padding:0}
html,body{width:1200px;height:2812px;overflow:hidden;background:var(--white)}
body{font-family:"Open Sans",Arial,sans-serif;color:var(--ink);position:relative}
.abs{position:absolute}
.house{background:linear-gradient(180deg,#b7c9d8 0%,#c9b79a 50%,#7e8a5e 100%)}

/* header + hero */
.hero{left:0;top:0;width:1200px;height:540px;background:linear-gradient(160deg,#b4c6d3 0%,#8a9485 35%,#5d6a4f 70%,#4a4f3e 100%)}
.logo-box{left:48px;top:0;width:140px;height:88px;background:var(--white);display:flex;align-items:center;justify-content:center;gap:8px;box-shadow:0 2px 6px rgba(0,0,0,.2)}
.logo-box .mark{width:14px;height:14px;background:var(--yellow)}
.logo-box .name{font-family:"Raleway",sans-serif;font-weight:800;font-size:28px;color:var(--grey)}
.nav{left:420px;top:14px;display:flex;gap:30px;font-size:11px;font-weight:600;color:var(--white);letter-spacing:.5px}
.headline{left:44px;top:300px;font-family:"Raleway",sans-serif;font-weight:700;font-size:46px;line-height:54px;color:var(--yellow);text-shadow:0 2px 4px rgba(0,0,0,.35)}
.dots{left:570px;top:508px;display:flex;gap:10px}
.dots i{width:9px;height:9px;border-radius:50%;background:rgba(255,255,255,.6)}
.dots i:first-child{background:var(--yellow)}

/* search */
.search{left:208px;top:560px;width:784px}
.search h4{font-size:11px;font-weight:700;color:var(--grey);letter-spacing:.4px}
.tabs{display:flex;margin-top:10px;gap:4px}
.tabs span{font-size:10px;padding:6px 14px;background:#f1f1f1;color:var(--muted)}
.tabs span.on{background:var(--yellow);color:var(--ink);font-weight:700}
.fields{display:grid;grid-template-columns:repeat(4,1fr);gap:10px;margin-top:12px}
.fields div{height:30px;border:1px solid var(--line);font-size:10px;color:var(--muted);padding:8px 10px;position:relative}
.fields div.sel::after{content:"";position:absolute;right:10px;top:12px;border:4px solid transparent;border-top-color:var(--muted)}
.fields div.go{border:0;background:var(--yellow);color:var(--ink);font-weight:700;text-align:center}
.search p{font-size:10px;font-weight:700;color:var(--grey);margin-top:12px}
.btn{display:inline-block;background:var(--yellow);font-size:10px;font-weight:700;color:var(--ink);padding:8px 22px}

/* featured */
.frame{left:160px;top:770px;width:880px;height:1250px;background:var(--yellow)}
.sec-title{font-family:"Raleway",sans-serif;font-size:30px;font-weight:600;color:var(--grey)}
.featured-title{left:208px;top:738px;background:var(--white);padding:0 10px 4px 0}
.feat{position:absolute}
.feat .cap{position:absolute;left:0;right:0;bottom:0;height:34px;background:rgba(251,195,10,.88);font-size:12px;font-weight:600;color:var(--white);padding:9px 12px;text-transform:uppercase}
.scroll{left:208px;top:1182px;width:784px;height:10px;background:#b0890a}
.scroll i{position:absolute;left:0;top:0;width:300px;height:10px;background:var(--dark)}

/* properties */
.props{left:208px;top:1236px;width:784px;height:770px;background:var(--white);padding:18px 0 0}
.filters{display:flex;gap:6px;margin-top:8px;position:relative}
.filters span{font-size:9px;padding:4px 12px;color:var(--muted)}
.filters span.on{background:var(--grey);color:var(--white)}
.pager{position:absolute;right:0;top:2px;display:flex;gap:5px}
.pager i{width:9px;height:9px;border:1px solid var(--muted)}
.grid{display:grid;grid-template-columns:repeat(3,248px);gap:20px 20px;margin-top:18px}
.card{border:1px solid var(--line);height:296px;position:relative}
.card .img{height:140px;position:relative}
.card .price{position:absolute;left:0;bottom:0;background:var(--yellow);font-size:11px;font-weight:700;padding:5px 10px;color:var(--ink)}
.card h5{font-size:12px;font-weight:700;color:var(--grey);margin:12px 12px 6px;text-transform:uppercase}
.card dl{margin:0 12px;font-size:10px;color:var(--muted)}
.card dl div{display:flex;justify-content:space-between;border-bottom:1px solid var(--line);padding:6px 0}
.card dd{color:var(--ink)}

/* manager cta */
.manager-title{left:208px;top:2040px;font-family:"Raleway",sans-serif;font-size:30px;font-weight:600;color:var(--grey)}
.cta{left:208px;top:2092px;width:784px;height:150px;background:var(--yellow);padding:26px 28px}
.cta p{font-family:"Raleway",sans-serif;font-weight:700;font-size:16px;line-height:22px;color:var(--grey);width:560px}
.cta .btn{background:var(--white);margin-top:18px}

/* about */
.about{left:208px;top:2280px;width:784px}
.about h3{font-family:"Raleway",sans-serif;font-size:22px;font-weight:600;color:var(--grey)}
.about p{font-size:10px;line-height:16px;color:var(--muted);margin-top:10px}
.about .btn{margin-top:14px}

/* footer */
.footer{left:0;top:2500px;width:1200px;height:262px;background:var(--dark)}
.col{position:absolute;top:28px;color:#bdbdbd;font-size:10px;line-height:18px}
.col h4{font-family:"Raleway",sans-serif;font-size:20px;font-weight:600;color:var(--yellow);margin-bottom:10px}
.subscribe{display:flex;margin-top:12px}
.subscribe span{width:190px;height:28px;background:var(--white);font-size:9px;color:var(--muted);padding:7px 10px}
.subscribe b{width:34px;height:28px;background:var(--yellow)}
.social{display:flex;gap:10px;margin-top:44px;margin-left:100px}
.social i{width:14px;height:14px;border-radius:50%;background:#6b6a6b}
.bottom{left:0;top:2762px;width:1200px;height:50px;background:var(--darker);color:#9a9a9a;font-size:9px;line-height:14px;padding:12px 208px}
.totop{left:1064px;top:2718px;width:30px;height:30px;border-radius:50%;background:#1f1f1f}
</style>
</head>
<body>

<section class="abs hero" role="img" aria-label="Aerial photo of a suburban neighbourhood with rows of houses and trees"></section>
<div class="abs logo-box"><span class="mark"></span><span class="name">Zenvok</span></div>
<nav class="abs nav"><span>PROPERTIES</span><span>OWNERS</span><span>ARE YOU A PROPERTY MANAGER</span><span>ABOUT US</span><span>CONTACT US</span></nav>
<h1 class="abs headline">Making renting YOUR<br>home an easy,<br>stress-free experience.</h1>
<div class="abs dots"><i></i><i></i><i></i><i></i><i></i></div>

<section class="abs search">
  <h4>FIND YOUR LOCAL PROPERTY MANAGER</h4>
  <div class="tabs"><span class="on">FOR RENT</span><span>FOR SALE</span></div>
  <div class="fields">
    <div>Keyword or City</div><div class="sel">Zip Code</div><div class="sel">Bedrooms</div><div class="sel">Bathrooms</div>
    <div class="sel">Min Price</div><div class="sel">Max Price</div><div class="sel">Property Type</div><div class="go">SEARCH</div>
  </div>
  <p>SEARCH OUR DIRECTORY TO FIND EXPERIENCED AND PROFESSIONAL PROPERTY MANAGEMENT COMPANIES THAT FIT YOUR NEEDS</p>
</section>

<div class="abs frame"></div>
<h2 class="abs sec-title featured-title">THIS MONTHS FEATURED PROPERTIES</h2>

<div class="feat" style="left:208px;top:790px;width:384px;height:330px"><div class="house" style="height:100%" role="img" aria-label="Photo of a large two-storey family home"></div><div class="cap">1235 Larkmoor Walk</div></div>
<div class="feat" style="left:608px;top:790px;width:184px;height:155px"><div class="house" style="height:100%" role="img" aria-label="Photo of a brick house"></div><div class="cap">2250 Brindle Rd</div></div>
<div class="feat" style="left:808px;top:790px;width:184px;height:155px"><div class="house" style="height:100%" role="img" aria-label="Photo of a suburban home"></div><div class="cap">2550 Ashvale</div></div>
<div class="feat" style="left:608px;top:962px;width:184px;height:158px"><div class="house" style="height:100%" role="img" aria-label="Photo of a family house"></div><div class="cap">1555 Brindle Rd</div></div>
<div class="feat" style="left:808px;top:962px;width:184px;height:158px"><div class="house" style="height:100%" role="img" aria-label="Photo of a home with garden"></div><div class="cap">2330 Quillmere</div></div>
<div class="abs scroll"><i></i></div>

<section class="abs props">
  <h2 class="sec-title">PROPERTIES</h2>
  <div class="filters"><span class="on">ALL</span><span>HOUSES</span><span>CONDOS</span><span>APARTMENTS</span><span>TOWNHOMES</span>
    <div class="pager"><i></i><i></i><i></i></div></div>
  <div class="grid">
    <article class="card"><div class="img house" role="img" aria-label="Photo of a brick house"><span class="price">$1,450/mo</span></div><h5>1235 Larkmoor Walk</h5><dl><div><dt>Bedrooms</dt><dd>3</dd></div><div><dt>Bathrooms</dt><dd>2</dd></div><div><dt>Square Footage</dt><dd>1,850</dd></div><div><dt>Type</dt><dd>Residential</dd></div></dl></article>
    <article class="card"><div class="img house" role="img" aria-label="Photo of a family home"><span class="price">$1,700/mo</span></div><h5>4850 Quillmere Blvd</h5><dl><div><dt>Bedrooms</dt><dd>4</dd></div><div><dt>Bathrooms</dt><dd>3</dd></div><div><dt>Square Footage</dt><dd>2,300</dd></div><div><dt>Type</dt><dd>Residential</dd></div></dl></article>
    <article class="card"><div class="img house" role="img" aria-label="Photo of a large house"><span class="price">$1,250/mo</span></div><h5>4450 Fernwick Row</h5><dl><div><dt>Bedrooms</dt><dd>3</dd></div><div><dt>Bathrooms</dt><dd>2</dd></div><div><dt>Square Footage</dt><dd>1,600</dd></div><div><dt>Type</dt><dd>Residential</dd></div></dl></article>
    <article class="card"><div class="img house" role="img" aria-label="Photo of a brick home"><span class="price">$1,350/mo</span></div><h5>1235 Larkmoor Walk</h5><dl><div><dt>Bedrooms</dt><dd>3</dd></div><div><dt>Bathrooms</dt><dd>2</dd></div><div><dt>Square Footage</dt><dd>1,700</dd></div><div><dt>Type</dt><dd>Residential</dd></div></dl></article>
    <article class="card"><div class="img house" role="img" aria-label="Photo of a suburban house"><span class="price">$1,550/mo</span></div><h5>4870 Oastley Dr</h5><dl><div><dt>Bedrooms</dt><dd>4</dd></div><div><dt>Bathrooms</dt><dd>2</dd></div><div><dt>Square Footage</dt><dd>2,050</dd></div><div><dt>Type</dt><dd>Residential</dd></div></dl></article>
    <article class="card"><div class="img house" role="img" aria-label="Photo of a house with lawn"><span class="price">$1,900/mo</span></div><h5>2250 Brindle Rd</h5><dl><div><dt>Bedrooms</dt><dd>4</dd></div><div><dt>Bathrooms</dt><dd>3</dd></div><div><dt>Square Footage</dt><dd>2,400</dd></div><div><dt>Type</dt><dd>Residential</dd></div></dl></article>
  </div>
</section>

<h2 class="abs manager-title">ARE YOU A PROPERTY MANAGER?</h2>
<section class="abs cta">
  <p>JOIN OUR REAL ESTATE PROPERTY MANAGEMENT COMPANY NETWORK. LET US HELP YOU FIND LEADS OF PROPERTY OWNERS SEEKING TO RENT THEIR HOMES.</p>
  <span class="btn">LEARN MORE</span>
</section>

<section class="abs about">
  <h3>About us</h3>
  <p>Zenvok connects property owners with trusted, local property managers. We review every company in our network so owners can compare services, fees and reviews in one place. Whether you own a single home or a growing portfolio, we make it simple to find a manager who handles tenants, rent collection, repairs and inspections with care. Property managers benefit too: our platform brings qualified leads from owners who are ready to rent, helping good companies grow their business in the neighbourhoods they know best. Our team is here to help both sides build lasting, stress-free partnerships.</p>
  <span class="btn">READ MORE</span>
</section>

<footer class="abs footer">
  <div class="col" style="left:208px;width:240px">
    <h4>Contact details</h4>
    Zenvok Property Network<br>410 Harbor Lane, Suite 12<br>Fairview, FL 30000<br><br>Phone: (555) 010-2468<br>Fax: (555) 010-1357<br>hello@zenvok.example
  </div>
  <div class="col" style="left:478px;width:220px">
    <h4>Useful links</h4>
    Are you a Property Manager?<br>Owner FAQ<br>Submit Your Listing<br>Site Map<br>Terms and Conditions<br>Privacy Policy<br>Customer Support
  </div>
  <div class="col" style="left:760px;width:232px">
    <h4>Stay Updated!</h4>
    Subscribe to our newsletter for the latest listings, tips and property news.
    <div class="subscribe"><span>Enter your email here</span><b></b></div>
    <div class="social"><i></i><i></i><i></i><i></i><i></i></div>
  </div>
</footer>
<div class="abs bottom">Copyright © 2015, Zenvok. All Rights Reserved.<br>Designed by Zenvok Studio</div>
<div class="abs totop"></div>

</body>
</html>
```